Book cover design : The Copper Lantern

We need a striking book cover design for a book which will be published via Orvello Reader and as a paperback. The book is a simple short story - ghost story - for children. The book is set in a contemporary English town.

The title of the book is : The Copper Lantern
The author is: Walter Finch

The book is a story book, for children, aged approximately 11-15 years old.
It is a ghost story, but not too scary.

Text to go on the front cover:
The Copper Lantern

Walter Finch

Text to go on the back cover :

The Copper Lantern; a ghost story of controlled readability for students aged 11 to 15 years, (catch-up reading). Also for students of English as a foreign language.

Target Market(s)

A ghost story of controlled readability for students aged 11 to 15 years, (catch-up reading). Also for students of English as a foreign language.

```html
<!DOCTYPE html>
<html lang="en">
<head>
<meta charset="utf-8">
<title>The Copper Lantern — Walter Finch</title>
<link href="https://fonts.googleapis.com/css2?family=Smokum&family=Oswald:wght@500&display=swap" rel="stylesheet">
<style>
  :root {
    --page: #ffffff;
    --mist: #b7d6c4;
    --moss: #557a66;
    --forest: #22382c;
    --night: #040605;
    --stone: #111412;
    --ink: #0d0f0e;
    --glow: #ffffff;
  }
  * { margin: 0; padding: 0; box-sizing: border-box; }
  html, body {
    width: 1200px;
    height: 1185px;
    overflow: hidden;
    background: var(--page);
  }
  .canvas {
    position: relative;
    width: 1200px;
    height: 1185px;
  }
  .cover {
    position: absolute;
    left: 261px;
    top: 86px;
    width: 686px;
    height: 1030px;
    overflow: hidden;
    font-family: "Smokum", "Oswald", "Arial Narrow", sans-serif;
  }
  .cover-scene {
    position: absolute;
    inset: 0;
    background:
      radial-gradient(ellipse 70% 45% at 60% 15%, var(--mist), rgba(183,214,196,0) 75%),
      radial-gradient(ellipse 30% 60% at 8% 60%, rgba(10,16,12,0.75), rgba(10,16,12,0) 80%),
      radial-gradient(ellipse 28% 60% at 95% 45%, rgba(10,16,12,0.7), rgba(10,16,12,0) 80%),
      linear-gradient(180deg, var(--moss) 0%, #3d5d4c 38%, var(--forest) 62%, var(--night) 100%);
  }
  .headstone {
    position: absolute;
    left: 133px;
    top: 240px;
    width: 388px;
    height: 730px;
    border-radius: 194px 194px 10px 10px;
    background: linear-gradient(180deg, #2a2e2c 0%, var(--stone) 55%, rgba(8,10,9,0.9) 100%);
    box-shadow: 0 0 40px rgba(0,0,0,0.5);
  }
  .ghost {
    position: absolute;
    left: 170px;
    top: 180px;
    width: 370px;
    height: 860px;
    border-radius: 50%;
    background:
      radial-gradient(ellipse 22% 12% at 55% 10%, rgba(255,255,255,1), rgba(255,255,255,0) 100%),
      radial-gradient(ellipse 40% 48% at 52% 52%, rgba(255,255,255,0.95), rgba(255,255,255,0.35) 60%, rgba(255,255,255,0) 100%);
    filter: blur(2px);
  }
  .author {
    position: absolute;
    top: 46px;
    left: 0;
    width: 100%;
    text-align: center;
    font-size: 58px;
    line-height: 1;
    letter-spacing: 2px;
    color: var(--ink);
    text-shadow: 0 0 8px var(--glow), 0 0 3px var(--glow);
  }
  .title { font-weight: 400; }
  .title-line {
    position: absolute;
    left: 0;
    width: 100%;
    text-align: center;
    line-height: 1;
    white-space: nowrap;
  }
  .title-lead {
    top: 516px;
    font-size: 120px;
    color: var(--ink);
    letter-spacing: 2px;
    text-shadow: 0 0 8px var(--glow), 0 0 3px var(--glow);
  }
  .title-main {
    font-size: 112px;
    color: var(--glow);
    letter-spacing: 4px;
    text-shadow: 0 0 16px rgba(255,255,255,0.85), -14px -12px 0 rgba(255,255,255,0.2);
  }
  .title-main.first { top: 632px; }
  .title-main.second { top: 742px; }
</style>
</head>
<body>
  <div class="canvas">
    <section class="cover">
      <div class="cover-scene" role="img" aria-label="Misty green graveyard at night with bare twisted trees, a cross-topped grave and an iron gate"></div>
      <div class="headstone" role="img" aria-label="Large dark arched headstone"></div>
      <div class="ghost" role="img" aria-label="Glowing white ghostly woman in a long fringed dress and beads, seen in silhouette"></div>
      <p class="author">WALTER FINCH</p>
      <h1 class="title">
        <span class="title-line title-lead">THE</span>
        <span class="title-line title-main first">COPPER</span>
        <span class="title-line title-main second">LANTERN</span>
      </h1>
    </section>
  </div>
</body>
</html>
```